Brightnest Stays Stationery Design

Letterpaper, business cards, notebook, envelope A4 & A5

Target Market(s)

Business, accommodation, hotels, flexible housing

Font styles to use
Other font styles liked:
• Montserrat

Colors

Designer to choose only greyscale colors for use in the design.

Requirements
Must have
• Luxurious appearance
Keep it simple, just like the logo
Modern
Nice to have
• Tight Luxury Design
Should not have
• Illustrations
Decorative

```html
<!DOCTYPE html>
<html lang="en">
<head>
<meta charset="utf-8">
<title>Brightnest Stays – Stationery</title>
<link href="https://fonts.googleapis.com/css2?family=Montserrat:wght@400;500&display=swap" rel="stylesheet">
<style>
  :root {
    --backdrop: #a7a8aa;
    --ink: #000000;
    --paper: #ffffff;
    --edge: #6d6e70;
    --ring: #9a9b9d;
    --ring-light: #e4e4e4;
  }
  * { margin: 0; padding: 0; box-sizing: border-box; }
  html, body { width: 1200px; height: 649px; overflow: hidden; }
  body {
    background: var(--backdrop);
    font-family: "Montserrat", sans-serif;
    color: var(--ink);
    position: relative;
  }
  .piece { position: absolute; }

  /* brand lockup: plain square + name */
  .brand { position: absolute; display: flex; flex-direction: column; align-items: center; font-weight: 400; }
  .brand__square { border: 1px solid currentColor; width: var(--sq, 22px); height: var(--sq-h, 26px); margin-bottom: var(--gap, 4px); }
  .brand__name { font-size: var(--name, 7px); letter-spacing: 0.06em; line-height: 1.1; white-space: nowrap; }
  .brand__sub { font-size: var(--sub, 3.6px); letter-spacing: 0.32em; line-height: 1.3; white-space: nowrap; }
  .on-dark { color: var(--paper); }
  .on-light { color: var(--ink); }

  /* business cards */
  .card { left: 94px; width: 163px; height: 105px; }
  .card--front { top: 36px; background: var(--ink); }
  .card--front .brand { left: 50%; top: 31px; transform: translateX(-50%); --sq: 22px; --sq-h: 26px; --name: 7px; --sub: 3.6px; }
  .card--back { top: 171px; background: var(--paper); }
  .card--back .brand { left: 51px; top: 32px; transform: translateX(-50%); --sq: 22px; --sq-h: 26px; --name: 7px; --sub: 3.6px; }
  .card__person { position: absolute; left: 101px; top: 28px; }
  .card__name { font-size: 6.5px; font-weight: 500; line-height: 1.2; }
  .card__role { font-size: 4px; line-height: 1.2; }
  .card__contact { position: absolute; left: 101px; top: 56px; font-size: 4.4px; line-height: 5.4px; }

  /* notebook */
  .notebook { left: 47px; top: 312px; width: 210px; height: 292px; background: var(--ink); border-radius: 14px; }
  .notebook .brand { left: 50%; top: 122px; transform: translateX(-50%); --sq: 25px; --sq-h: 30px; --gap: 5px; --name: 8px; --sub: 4px; }
  .notebook__web { position: absolute; left: 0; right: 0; top: 255px; text-align: center; color: var(--paper); font-size: 5px; letter-spacing: 0.22em; }
  .spiral { position: absolute; left: 30px; top: 340px; }

  /* letterhead */
  .letterhead { left: 287px; top: 36px; width: 402px; height: 569px; background: var(--paper); }
  .letterhead .brand { left: 55px; top: 28px; transform: translateX(-50%); --sq: 25px; --sq-h: 30px; --gap: 5px; --name: 8px; --sub: 4px; }
  .letterhead__contact { position: absolute; left: 55px; top: 84px; transform: translateX(-50%); text-align: center; font-size: 5px; line-height: 7.5px; white-space: nowrap; }

  /* envelopes */
  .envelope { left: 718px; width: 438px; height: 195px; background: var(--paper); border: 0.6px solid var(--edge); }
  .envelope--back { top: 36px; }
  .envelope__flap { position: absolute; left: 0; top: 0; }
  .envelope--front { top: 263px; }
  .envelope--front .brand { left: 44px; top: 131px; transform: translateX(-50%); --sq: 25px; --sq-h: 30px; --gap: 5px; --name: 8px; --sub: 4px; }
  .envelope__contact { position: absolute; left: 87px; top: 165px; font-size: 4.8px; line-height: 7px; white-space: nowrap; }
</style>
</head>
<body>

  <section class="piece card card--front">
    <div class="brand on-dark">
      <span class="brand__square"></span>
      <span class="brand__name">BRIGHTNEST</span>
      <span class="brand__sub">STAYS</span>
    </div>
  </section>

  <section class="piece card card--back">
    <div class="brand on-light">
      <span class="brand__square"></span>
      <span class="brand__name">BRIGHTNEST</span>
      <span class="brand__sub">STAYS</span>
    </div>
    <div class="card__person">
      <p class="card__name">Name Here</p>
      <p class="card__role">Role / Position</p>
    </div>
    <div class="card__contact">
      <p>123 Street Name, City</p>
      <p>email@email.com</p>
      <p>+1 888 888 8888</p>
      <p>www.mywebsite.com</p>
    </div>
  </section>

  <section class="piece notebook">
    <div class="brand on-dark">
      <span class="brand__square"></span>
      <span class="brand__name">BRIGHTNEST</span>
      <span class="brand__sub">STAYS</span>
    </div>
    <p class="notebook__web">www.mywebsite.com</p>
  </section>

  <svg class="spiral" width="36" height="236" viewBox="0 0 36 236" aria-hidden="true">
    <defs>
      <linearGradient id="ringWire" x1="0" x2="1">
        <stop offset="0" stop-color="var(--ring-light)" stop-opacity="0.3"/>
        <stop offset="1" stop-color="var(--ring-light)"/>
      </linearGradient>
    </defs>
    <g id="rings">
      <g transform="translate(0,8)"><rect x="4" y="-1.2" width="24" height="2.4" rx="1.2" fill="url(#ringWire)"/><circle cx="29" cy="0" r="3.6" fill="var(--ring)"/></g>
      <g transform="translate(0,26.3)"><rect x="4" y="-1.2" width="24" height="2.4" rx="1.2" fill="url(#ringWire)"/><circle cx="29" cy="0" r="3.6" fill="var(--ring)"/></g>
      <g transform="translate(0,44.6)"><rect x="4" y="-1.2" width="24" height="2.4" rx="1.2" fill="url(#ringWire)"/><circle cx="29" cy="0" r="3.6" fill="var(--ring)"/></g>
      <g transform="translate(0,62.9)"><rect x="4" y="-1.2" width="24" height="2.4" rx="1.2" fill="url(#ringWire)"/><circle cx="29" cy="0" r="3.6" fill="var(--ring)"/></g>
      <g transform="translate(0,81.2)"><rect x="4" y="-1.2" width="24" height="2.4" rx="1.2" fill="url(#ringWire)"/><circle cx="29" cy="0" r="3.6" fill="var(--ring)"/></g>
      <g transform="translate(0,99.5)"><rect x="4" y="-1.2" width="24" height="2.4" rx="1.2" fill="url(#ringWire)"/><circle cx="29" cy="0" r="3.6" fill="var(--ring)"/></g>
      <g transform="translate(0,117.8)"><rect x="4" y="-1.2" width="24" height="2.4" rx="1.2" fill="url(#ringWire)"/><circle cx="29" cy="0" r="3.6" fill="var(--ring)"/></g>
      <g transform="translate(0,136.1)"><rect x="4" y="-1.2" width="24" height="2.4" rx="1.2" fill="url(#ringWire)"/><circle cx="29" cy="0" r="3.6" fill="var(--ring)"/></g>
      <g transform="translate(0,154.4)"><rect x="4" y="-1.2" width="24" height="2.4" rx="1.2" fill="url(#ringWire)"/><circle cx="29" cy="0" r="3.6" fill="var(--ring)"/></g>
      <g transform="translate(0,172.7)"><rect x="4" y="-1.2" width="24" height="2.4" rx="1.2" fill="url(#ringWire)"/><circle cx="29" cy="0" r="3.6" fill="var(--ring)"/></g>
      <g transform="translate(0,191)"><rect x="4" y="-1.2" width="24" height="2.4" rx="1.2" fill="url(#ringWire)"/><circle cx="29" cy="0" r="3.6" fill="var(--ring)"/></g>
      <g transform="translate(0,209.3)"><rect x="4" y="-1.2" width="24" height="2.4" rx="1.2" fill="url(#ringWire)"/><circle cx="29" cy="0" r="3.6" fill="var(--ring)"/></g>
      <g transform="translate(0,227.6)"><rect x="4" y="-1.2" width="24" height="2.4" rx="1.2" fill="url(#ringWire)"/><circle cx="29" cy="0" r="3.6" fill="var(--ring)"/></g>
    </g>
  </svg>

  <section class="piece letterhead">
    <div class="brand on-light">
      <span class="brand__square"></span>
      <span class="brand__name">BRIGHTNEST</span>
      <span class="brand__sub">STAYS</span>
    </div>
    <div class="letterhead__contact">
      <p>123 Street Name, City</p>
      <p>email@email.com</p>
      <p>+1 888 888 8888</p>
      <p>www.mywebsite.com</p>
    </div>
  </section>

  <section class="piece envelope envelope--back">
    <svg class="envelope__flap" width="438" height="57" viewBox="0 0 438 57" aria-hidden="true">
      <path d="M0 0 H438 L433 44 Q432 56 420 56 H18 Q6 56 5 44 Z" fill="var(--ink)"/>
    </svg>
  </section>

  <section class="piece envelope envelope--front">
    <div class="brand on-light">
      <span class="brand__square"></span>
      <span class="brand__name">BRIGHTNEST</span>
      <span class="brand__sub">STAYS</span>
    </div>
    <div class="envelope__contact">
      <p>123 Street Name, City</p>
      <p>email@email.com | +1 888 888 8888 | www.mywebsite.com</p>
    </div>
  </section>

</body>
</html>
```